13 Tavo - new website design project

Our company Tavo Electrical is developing a new lead generation website focused on Electrical, LED Lighting and Solar Power. We need a high converting website.

Example of our current website is www.tavoelectrical.com.au You can take content from this website for this new design. Our colours are red, black and white. For our new website we would like to promote Tavo, Bright Days Ahead. Please listen to the jingle.

The below link is the company jingle that we have developed.
http://www.tunecraftaudio.com.au/tav-tc-v1/

The key for this brief is to generate leads for Electrical, LED Lighting (for commercial) and Solar Power & Storage.

Target Market(s)

Business owners in Melbourne Victoria

Number of Pages Required

4 page

Colors
ec1f27
ffffff

Requirements
Must have
• This page must be clean, be in line with company branding and a high converting lead website.

```html
<!DOCTYPE html>
<html lang="en">
<head>
<meta charset="utf-8">
<title>Tavo Electrical – Electrical, LED Lighting &amp; Solar Power</title>
<link rel="stylesheet" href="https://fonts.googleapis.com/css2?family=Open+Sans:wght@400;600;700;800&display=swap">
<style>
:root{
  --red:#c8202a;
  --red-bright:#ec1f27;
  --ink:#3a3a3a;
  --text:#555;
  --dark:#2f2f2f;
  --tab:#3b3b3b;
  --grey-bg:#f2f2f2;
  --white:#fff;
  --footer-text:#bdbdbd;
}
*{margin:0;padding:0;box-sizing:border-box}
html,body{width:1200px;height:2731px;overflow:hidden}
body{position:relative;font-family:"Open Sans",Arial,sans-serif;color:var(--text);background:var(--white)}
.abs{position:absolute}

/* header */
.site-header{position:absolute;left:0;top:0;width:1200px;height:127px;background:var(--white);border-top:5px solid var(--red)}
.brand{position:absolute;left:76px;top:18px;display:flex;align-items:center;gap:12px}
.brand-dot{width:34px;height:34px;border-radius:50%;background:var(--red)}
.brand-name{font-size:44px;font-weight:800;color:var(--ink);letter-spacing:1px;line-height:1}
.brand-tag{position:absolute;left:76px;top:72px;font-size:15px;font-weight:600;color:var(--ink)}
.phone-box{position:absolute;left:885px;top:-5px;width:240px;height:63px;background:var(--red);color:var(--white);font-weight:700;font-size:25px;display:flex;align-items:center;justify-content:center;gap:10px}
.service-tabs{position:absolute;left:286px;top:82px;display:flex;gap:4px}
.service-tabs a{display:block;height:45px;line-height:47px;padding:0 22px;background:var(--tab);color:var(--white);font-size:13px;font-weight:700;text-decoration:none}
.main-nav{position:absolute;top:91px;left:727px;display:flex;gap:30px}
.main-nav a{font-size:13px;font-weight:700;color:var(--ink);text-decoration:none}
.main-nav a.active{color:var(--red-bright)}

/* hero */
.hero{position:absolute;left:0;top:127px;width:1200px;height:523px;background:linear-gradient(160deg,#5ea6e8 0%,#9fd0f4 30%,#2c5fa8 55%,#163f84 80%,#4f7a3b 100%)}
.hero-label{position:absolute;left:75px;top:221px;width:419px;height:85px;background:rgba(30,30,30,.85);color:var(--white);font-size:48px;font-weight:700;letter-spacing:2px;line-height:85px;padding-left:22px}
.hero-dots{position:absolute;left:72px;top:467px;display:flex;gap:10px}
.hero-dots span{width:12px;height:12px;border-radius:50%;background:var(--white)}
.hero-dots span.on{background:var(--red)}

/* sections */
.section-title{position:absolute;left:0;width:1200px;text-align:center;font-size:50px;font-weight:800;color:var(--ink);letter-spacing:1px}
.about{position:absolute;left:0;top:1047px;width:1200px;height:355px;background:var(--grey-bg)}
.about p{position:absolute;left:80px;top:118px;width:1040px;text-align:center;font-size:16.5px;line-height:29px;color:var(--text)}
.btn{position:absolute;left:497px;top:239px;width:206px;height:56px;background:var(--red);color:var(--white);font-size:17px;font-weight:700;text-align:center;line-height:56px}

.why{position:absolute;left:0;top:1402px;width:1200px;height:506px;background:var(--white)}
.why-card{position:absolute;top:129px;width:331px;height:317px;background:var(--white);border:1px solid #e2e2e2;border-bottom:5px solid var(--red);box-shadow:0 2px 4px rgba(0,0,0,.08);text-align:center}
.why-card .icon{width:94px;height:94px;margin:23px auto 0;border-radius:50%;background:var(--red);display:flex;align-items:center;justify-content:center}
.why-card h3{margin-top:22px;font-size:22px;font-weight:700;color:var(--red)}
.why-card p{margin:8px auto 0;width:282px;font-size:15px;line-height:29px;color:var(--text)}
.why-arrow{position:absolute;top:268px}

.testimonials{position:absolute;left:0;top:1908px;width:1200px;height:317px;background:var(--grey-bg)}
.testi-media{position:absolute;left:75px;top:57px;width:308px;height:198px;background:var(--white)}
.testi-brand{height:68px;display:flex;align-items:center;padding-left:18px}
.testi-brand .name{font-size:30px;font-weight:700;color:var(--ink)}
.testi-photo{height:130px;background:linear-gradient(180deg,#cfd6dc,#6c7a86 55%,#3c4650)}
.testi-title{position:absolute;left:435px;top:50px;font-size:50px;font-weight:800;color:var(--ink);letter-spacing:1px}
.testi-quote{position:absolute;left:435px;top:139px;width:690px;font-size:17px;line-height:31px;color:var(--text)}
.testi-name{position:absolute;left:435px;top:206px;font-size:17px;font-weight:700;color:var(--red)}
.testi-place{position:absolute;left:435px;top:238px;font-size:17px;color:var(--text)}
.testi-arrows{position:absolute;left:1078px;top:64px}

.clients{position:absolute;left:0;top:2225px;width:1200px;height:272px;background:var(--white)}
.clients h2{position:absolute;left:0;top:43px;width:1200px;text-align:center;font-size:37px;font-weight:800;color:var(--ink);letter-spacing:1px}
.client{position:absolute;top:119px;width:205px;height:114px;display:flex;align-items:center;justify-content:center;font-size:24px;font-weight:700;text-align:center;white-space:nowrap}

.site-footer{position:absolute;left:0;top:2497px;width:1200px;height:234px;background:var(--dark)}
.foot-brand{position:absolute;left:76px;top:47px;display:flex;align-items:center;gap:10px}
.foot-brand .brand-dot{width:28px;height:28px;background:#8a8a8a}
.foot-brand .brand-name{font-size:40px;color:#9a9a9a}
.foot-tag{position:absolute;left:76px;top:102px;font-size:14px;font-weight:600;color:#9a9a9a}
.copyright{position:absolute;left:76px;top:148px;font-size:13px;line-height:22px;color:var(--footer-text)}
.foot-col{position:absolute;top:46px}
.foot-col h4{font-size:14px;font-weight:700;color:var(--white);margin-bottom:12px;letter-spacing:.5px}
.foot-col li{list-style:none;font-size:12px;color:var(--footer-text);line-height:30px}
.socials{display:flex;gap:14px;margin-top:4px}
.socials span{width:18px;height:18px;border-radius:3px;background:#9a9a9a}
.foot-phone{position:absolute;left:925px;top:137px;font-size:25px;font-weight:700;color:var(--white);display:flex;align-items:center;gap:10px}
</style>
</head>
<body>

<header class="site-header">
  <div class="brand"><span class="brand-dot"></span><span class="brand-name">TAVO</span></div>
  <div class="brand-tag">Bright Days Ahead</div>
  <div class="phone-box">
    <svg width="22" height="22" viewBox="0 0 24 24"><path fill="#fff" d="M6.6 10.8a15.1 15.1 0 0 0 6.6 6.6l2.2-2.2c.3-.3.7-.4 1-.2 1.1.4 2.3.6 3.6.6.6 0 1 .4 1 1V20c0 .6-.4 1-1 1A17 17 0 0 1 3 4c0-.6.4-1 1-1h3.5c.6 0 1 .4 1 1 0 1.3.2 2.5.6 3.6.1.3 0 .7-.2 1z"/></svg>
    137926 TAVO
  </div>
  <nav class="service-tabs"><a>ELECTRICAL</a><a>LED LIGHTING</a><a>SOLAR POWER</a></nav>
  <nav class="main-nav"><a class="active">HOME</a><a>TAVO STORY</a><a>OUR WORK</a><a>CONTACT US</a></nav>
</header>

<section class="hero" role="img" aria-label="Rows of solar panels under a blue sky with wind turbines behind">
  <div class="hero-label">SOLAR POWER</div>
  <div class="hero-dots"><span class="on"></span><span></span><span></span></div>
</section>

<section class="services">
  <svg class="abs" style="left:0;top:650px" width="1200" height="397" viewBox="0 650 1200 397">
    <defs>
      <linearGradient id="g-elec" x1="0" y1="0" x2="1" y2="1"><stop offset="0" stop-color="#c9ccd0"/><stop offset="1" stop-color="#3b4a5e"/></linearGradient>
      <linearGradient id="g-led" x1="0" y1="0" x2="0" y2="1"><stop offset="0" stop-color="#5e8d3a"/><stop offset="1" stop-color="#a7a9ab"/></linearGradient>
      <linearGradient id="g-solar" x1="0" y1="0" x2="0" y2="1"><stop offset="0" stop-color="#9cc4ea"/><stop offset=".55" stop-color="#4d5f74"/><stop offset="1" stop-color="#5c8a3c"/></linearGradient>
    </defs>
    <g role="img" aria-label="Electrician working on a switchboard">
      <polygon points="119,705 421,705 377,989 75,989" fill="url(#g-elec)"/>
      <polygon points="87,920 387,920 377,989 75,989" fill="rgba(30,30,30,.8)"/>
      <polygon points="119,705 421,705 377,989 75,989" fill="none" stroke="#c8202a" stroke-width="6"/>
      <text x="231" y="965" text-anchor="middle" font-family="Open Sans, sans-serif" font-weight="700" font-size="25" fill="#fff" letter-spacing="1">ELECTRICAL</text>
    </g>
    <g role="img" aria-label="Close-up of LED light bulbs">
      <polygon points="470,705 770,705 726,989 426,989" fill="url(#g-led)"/>
      <polygon points="437,920 737,920 726,989 426,989" fill="rgba(30,30,30,.8)"/>
      <polygon points="470,705 770,705 726,989 426,989" fill="none" stroke="#c8202a" stroke-width="6"/>
      <text x="582" y="965" text-anchor="middle" font-family="Open Sans, sans-serif" font-weight="700" font-size="25" fill="#fff" letter-spacing="1">LED LIGHTING</text>
    </g>
    <g role="img" aria-label="Solar panel array in a green field">
      <polygon points="823,705 1124,705 1080,989 779,989" fill="url(#g-solar)"/>
      <polygon points="790,920 1091,920 1080,989 779,989" fill="rgba(30,30,30,.8)"/>
      <polygon points="823,705 1124,705 1080,989 779,989" fill="none" stroke="#c8202a" stroke-width="6"/>
      <text x="935" y="965" text-anchor="middle" font-family="Open Sans, sans-serif" font-weight="700" font-size="25" fill="#fff" letter-spacing="1">SOLAR POWER</text>
    </g>
  </svg>
</section>

<section class="about">
  <h2 class="section-title" style="top:40px">ABOUT US</h2>
  <p>Tavo Electrical was formed to be an expert Electricity Contracting Company providing services to all Residential and Commercial Customers. With over 10 years of experience, Tavo Electrical has developed a highly-experienced team of professionals that<br>ensure all our customer expectations are met.</p>
  <div class="btn">READ MORE</div>
</section>

<section class="why">
  <h2 class="section-title" style="top:42px">WHY CHOOSE US?</h2>
  <svg class="why-arrow" style="left:44px" width="20" height="32" viewBox="0 0 20 32"><path d="M16 3 4 16l12 13" fill="none" stroke="#bbb" stroke-width="4"/></svg>
  <svg class="why-arrow" style="left:1138px" width="20" height="32" viewBox="0 0 20 32"><path d="m4 3 12 13L4 29" fill="none" stroke="#bbb" stroke-width="4"/></svg>

  <div class="why-card" style="left:75px">
    <div class="icon"><svg width="46" height="34" viewBox="0 0 46 34"><rect x="2" y="4" width="42" height="26" fill="none" stroke="#fff" stroke-width="4"/><circle cx="23" cy="17" r="7" fill="none" stroke="#fff" stroke-width="3"/></svg></div>
    <h3>Value for Money</h3>
    <p>We provide extremely competitive pricing, which means you get value for money on quality that is comparable to the best in the industry.</p>
  </div>
  <div class="why-card" style="left:435px">
    <div class="icon"><svg width="46" height="46" viewBox="0 0 46 46"><path d="M23 6 13 22M10 28h20M36 22 28 10" fill="none" stroke="#fff" stroke-width="5"/><path d="m8 18 5 5 4-7M26 33l5-5-5-5M30 7l-3 5 6 1" fill="none" stroke="#fff" stroke-width="3"/></svg></div>
    <h3>Environmentally Friendly</h3>
    <p>We a committed to reducing carbon emissions by installing Solar Power and upgrading sites to LED Lighting.<br>In addition to reducing the carbon..</p>
  </div>
  <div class="why-card" style="left:794px">
    <div class="icon"><svg width="46" height="46" viewBox="0 0 46 46"><path d="M4 22a19 19 0 0 1 38 0z" fill="#fff"/><path d="M23 22v15a4 4 0 0 1-8 0" fill="none" stroke="#fff" stroke-width="3"/></svg></div>
    <h3>Fully Insured</h3>
    <p>Tavo Electrical is fully insured and equipped to handle break downs and service call outs.</p>
  </div>
</section>

<section class="testimonials">
  <div class="testi-media">
    <div class="testi-brand"><span class="name">Norvastel</span></div>
    <div class="testi-photo" role="img" aria-label="Interior of a large industrial warehouse with bright overhead lighting"></div>
  </div>
  <h2 class="testi-title">TESTIMONIALS</h2>
  <svg class="testi-arrows" width="48" height="28" viewBox="0 0 48 28"><path d="M14 3 4 14l10 11M34 3l10 11-10 11" fill="none" stroke="#aaa" stroke-width="4"/></svg>
  <p class="testi-quote"><strong style="color:#444">&#8220;</strong> Excellent work and very professional. Marcus takes time to explain everything and demonstrate workings. Very clear precise and accurate.&#8221;</p>
  <div class="testi-name">Dlenk</div>
  <div class="testi-place">Cranbourne North VIC</div>
</section>

<section class="clients">
  <h2>OUR SATISFIED CLIENTS INCLUDE...</h2>
  <div class="client" style="left:131px;color:var(--red)">Velvetmart</div>
  <div class="client" style="left:370px;color:var(--ink)">Outback Supplies</div>
  <div class="client" style="left:615px;color:var(--red)">Heron Plumbing</div>
  <div class="client" style="left:860px;color:var(--red)">Golden Grill</div>
</section>

<footer class="site-footer">
  <div class="foot-brand"><span class="brand-dot"></span><span class="brand-name">TAVO</span></div>
  <div class="foot-tag">Bright Days Ahead</div>
  <div class="copyright">Copyright © 2017 All Rights Reserved<br>Privacy Policy</div>
  <div class="foot-col" style="left:388px"><h4>SITE MAP</h4><ul><li>HOME</li><li>TAVO STORY</li><li>OUR WORK</li><li>CONTACT US</li></ul></div>
  <div class="foot-col" style="left:543px"><h4>QUICK LINKS</h4><ul><li>LED LIGHTING</li><li>SOLAR POWER</li><li>ELECTRICAL</li><li>CAREER</li></ul></div>
  <div class="foot-col" style="left:719px"><h4>OTHERS</h4><ul><li>TERMS AND CONDITIONS</li><li>PRIVACY</li></ul></div>
  <div class="foot-col" style="left:925px"><h4>CONNECT US</h4><div class="socials"><span></span><span></span><span></span><span></span><span></span></div></div>
  <div class="foot-phone">
    <svg width="22" height="22" viewBox="0 0 24 24"><path fill="#fff" d="M6.6 10.8a15.1 15.1 0 0 0 6.6 6.6l2.2-2.2c.3-.3.7-.4 1-.2 1.1.4 2.3.6 3.6.6.6 0 1 .4 1 1V20c0 .6-.4 1-1 1A17 17 0 0 1 3 4c0-.6.4-1 1-1h3.5c.6 0 1 .4 1 1 0 1.3.2 2.5.6 3.6.1.3 0 .7-.2 1z"/></svg>
    137926 TAVO
  </div>
</footer>

</body>
</html>
```